Single-sided business card for restaurant bellwether with new logo made on this site

Business card options with new logo including restaurant name, address, phone number and website. This business card is single-sided only and will be presented at the hostess desk for clients to take. I would like to see options based on a cream card background, a white card background, a yellow card background and a burgundy colored background. It needs to be elegant and traditional.

Target Market(s)

local and international crowd

Industry/Entity Type

restaurant

Contact Information for Business Card

address, website and phone number

Font styles to use
Serif

Colors
EE7325
F08F49
F5BC92
FAE3D3
FDF4ED

Requirements
Must have
• new logo, address, phone number, website
Should not have
• more than three colors

```html
<!DOCTYPE html>
<html lang="es">
<head>
<meta charset="utf-8">
<title>Bellwether – Business Card</title>
<link rel="stylesheet" href="https://fonts.googleapis.com/css2?family=Bitter:wght@400;500&display=swap">
<style>
  :root {
    --backdrop: #2e2e2e;
    --card-white: #f7f7f6;
    --card-yellow: #eaaa28;
    --ink-brown: #3b1613;
    --ink-cream: #fdf4ed;
    --accent-gold: #e9a826;
    --rule-light: rgba(253, 244, 237, 0.55);
  }
  * { box-sizing: border-box; margin: 0; padding: 0; }
  html, body {
    width: 1200px;
    height: 900px;
    overflow: hidden;
    background: var(--backdrop);
    font-family: "Bitter", Georgia, serif;
  }
  .stage {
    position: relative;
    width: 1200px;
    height: 900px;
  }
  .card {
    position: absolute;
    width: 630px;
    height: 360px;
    border-radius: 26px;
    overflow: hidden;
  }
  .card--front {
    left: 90px;
    top: 80px;
    background: var(--card-white);
  }
  .card--back {
    left: 480px;
    top: 460px;
    background: var(--card-yellow);
  }

  .brand {
    position: absolute;
    display: flex;
    flex-direction: column;
    align-items: center;
    gap: 22px;
  }
  .card--front .brand { left: 70px; top: 78px; }
  .card--back .brand { left: 50px; top: 92px; }

  .brand__square {
    width: 120px;
    height: 120px;
  }
  .card--front .brand__square { background: var(--accent-gold); }
  .card--back .brand__square { background: var(--ink-cream); width: 104px; height: 104px; }

  .brand__name {
    font-weight: 500;
    font-size: 34px;
    letter-spacing: 0.16em;
    text-transform: uppercase;
    line-height: 1;
  }
  .card--front .brand__name { color: var(--ink-brown); }
  .card--back .brand__name { color: var(--ink-cream); font-size: 28px; }

  .divider {
    position: absolute;
    left: 290px;
    top: 70px;
    width: 1px;
    height: 220px;
    background: linear-gradient(to bottom, transparent, var(--rule-light), transparent);
  }

  .contact {
    position: absolute;
    left: 320px;
    top: 118px;
    list-style: none;
    display: flex;
    flex-direction: column;
    gap: 20px;
    color: var(--ink-cream);
    font-size: 17px;
    line-height: 1.35;
  }
  .contact__item {
    display: flex;
    align-items: flex-start;
    gap: 12px;
  }
  .contact__icon {
    flex: none;
    width: 18px;
    height: 18px;
    margin-top: 2px;
    fill: var(--ink-brown);
  }
</style>
</head>
<body>
<main class="stage">

  <section class="card card--front" aria-label="Card front">
    <div class="brand">
      <div class="brand__square"></div>
      <p class="brand__name">Bellwether</p>
    </div>
  </section>

  <section class="card card--back" aria-label="Card back">
    <div class="brand">
      <div class="brand__square"></div>
      <p class="brand__name">Bellwether</p>
    </div>

    <div class="divider"></div>

    <ul class="contact">
      <li class="contact__item">
        <svg class="contact__icon" viewBox="0 0 24 24" aria-hidden="true">
          <path d="M6.6 10.8a15.1 15.1 0 0 0 6.6 6.6l2.2-2.2a1 1 0 0 1 1-.25 11.4 11.4 0 0 0 3.6.57 1 1 0 0 1 1 1V20a1 1 0 0 1-1 1A17 17 0 0 1 3 4a1 1 0 0 1 1-1h3.5a1 1 0 0 1 1 1c0 1.25.2 2.45.57 3.57a1 1 0 0 1-.25 1z"/>
        </svg>
        <span>958-555-0142</span>
      </li>
      <li class="contact__item">
        <svg class="contact__icon" viewBox="0 0 24 24" aria-hidden="true">
          <path d="M12 2a10 10 0 1 0 0 20 10 10 0 0 0 0-20zm6.9 6h-3a15.6 15.6 0 0 0-1.4-3.6A8 8 0 0 1 18.9 8zM12 4c.8 1.2 1.5 2.5 1.9 4h-3.8c.4-1.5 1.1-2.8 1.9-4zM4.3 14a8.2 8.2 0 0 1 0-4h3.4a16 16 0 0 0 0 4zm.8 2h3a15.6 15.6 0 0 0 1.4 3.6A8 8 0 0 1 5.1 16zM8 8H5.1a8 8 0 0 1 4.4-3.6A15.6 15.6 0 0 0 8 8zm4 12c-.8-1.2-1.5-2.5-1.9-4h3.8c-.4 1.5-1.1 2.8-1.9 4zm2.3-6H9.7a14.7 14.7 0 0 1 0-4h4.6a14.7 14.7 0 0 1 0 4zm.2 5.6a15.6 15.6 0 0 0 1.4-3.6h3a8 8 0 0 1-4.4 3.6zm1.8-5.6a16 16 0 0 0 0-4h3.4a8.2 8.2 0 0 1 0 4z"/>
        </svg>
        <span>www.bellwether.com.mx</span>
      </li>
      <li class="contact__item">
        <svg class="contact__icon" viewBox="0 0 24 24" aria-hidden="true">
          <path d="M12 2a7 7 0 0 0-7 7c0 5.2 7 13 7 13s7-7.8 7-13a7 7 0 0 0-7-7zm0 9.5A2.5 2.5 0 1 1 12 6.5a2.5 2.5 0 0 1 0 5z"/>
        </svg>
        <span>Magnolia 417<br>Bahías del Sol, Oaxaca CP 70910</span>
      </li>
    </ul>
  </section>

</main>
</body>
</html>
```